BrickaFun Business Card

We need a business card design for our company. We sell construction-themed amusement rides for kids.

Contact Information for Business Card

Contact info on business card should include:
Dale Hurst
Co-Founder & COO
(833) 517-BRICKAF
Dale@brickafun.com
www.brickafun.com

```html
<!DOCTYPE html>
<html lang="en">
<head>
<meta charset="utf-8">
<title>BrickaFun Business Card</title>
<link rel="stylesheet" href="https://fonts.googleapis.com/css2?family=Lato:wght@400;700;900&display=swap">
<style>
  :root {
    --bg: #e9e7e4;
    --card-dark: #070707;
    --card-light: #ffffff;
    --orange: #f07a1f;
    --purple: #7b2f9a;
    --ink: #3a3a3a;
    --muted: #555555;
  }
  * { margin: 0; padding: 0; box-sizing: border-box; }
  html, body { width: 1200px; height: 847px; overflow: hidden; }
  body {
    background: var(--bg);
    font-family: "Lato", sans-serif;
    display: flex;
    align-items: center;
    justify-content: center;
    gap: 48px;
  }
  .card {
    width: 540px;
    height: 309px;
    position: relative;
    border-bottom: 4px solid var(--orange);
    border-right: 2px solid var(--orange);
    box-shadow: 0 10px 24px rgba(0,0,0,0.18);
  }
  .card-front { background: var(--card-dark); }
  .card-back { background: var(--card-light); }

  .brand {
    display: flex;
    align-items: center;
    gap: 12px;
    position: absolute;
  }
  .brand-name {
    font-weight: 900;
    color: var(--orange);
    letter-spacing: 0.5px;
    line-height: 1;
  }
  .brand-mark {
    border-radius: 50%;
    background: var(--purple);
    flex: none;
  }
  .card-front .brand { left: 50%; top: 50%; transform: translate(-50%, -50%); }
  .card-front .brand-name { font-size: 64px; }
  .card-front .brand-mark { width: 46px; height: 46px; }

  .card-back .brand { left: 60px; top: 42px; }
  .card-back .brand-name { font-size: 62px; }
  .card-back .brand-mark { width: 44px; height: 44px; }

  .holder { position: absolute; left: 60px; top: 140px; }
  .holder-name { font-size: 22px; font-weight: 700; letter-spacing: 0.5px; }
  .holder-first { color: var(--orange); }
  .holder-last { color: var(--purple); }
  .holder-role { font-size: 15px; color: var(--muted); margin-top: 4px; }

  .contacts { position: absolute; left: 60px; top: 210px; list-style: none; }
  .contacts li {
    display: flex; align-items: center; gap: 10px;
    font-size: 15px; color: var(--ink); line-height: 22px;
  }
  .contacts .no-icon { padding-left: 24px; }
  .contacts svg { width: 14px; height: 14px; flex: none; }
</style>
</head>
<body>
  <section class="card card-front">
    <div class="brand">
      <span class="brand-name">BrickaFun</span>
      <span class="brand-mark"></span>
    </div>
  </section>

  <section class="card card-back">
    <div class="brand">
      <span class="brand-name">BrickaFun</span>
      <span class="brand-mark"></span>
    </div>

    <div class="holder">
      <p class="holder-name"><span class="holder-first">DALE</span> <span class="holder-last">HURST</span></p>
      <p class="holder-role">Co-Founder &amp; COO</p>
    </div>

    <ul class="contacts">
      <li>
        <svg viewBox="0 0 24 24" aria-hidden="true"><path fill="var(--orange)" d="M6.6 10.8a15 15 0 0 0 6.6 6.6l2.2-2.2a1 1 0 0 1 1-.25 11.4 11.4 0 0 0 3.6.57 1 1 0 0 1 1 1V20a1 1 0 0 1-1 1A17 17 0 0 1 3 4a1 1 0 0 1 1-1h3.5a1 1 0 0 1 1 1c0 1.25.2 2.45.57 3.57a1 1 0 0 1-.25 1z"/></svg>
        (833) 517-BRICKAF
      </li>
      <li>
        <svg viewBox="0 0 24 24" aria-hidden="true"><rect x="2" y="5" width="20" height="14" rx="1" fill="var(--orange)"/><path d="M3 6l9 7 9-7" fill="none" stroke="#fff" stroke-width="1.6"/></svg>
        Dale@brickafun.com
      </li>
      <li>
        <svg viewBox="0 0 24 24" aria-hidden="true"><circle cx="12" cy="12" r="10" fill="var(--orange)"/><path d="M2 12h20M12 2c3 3 3 17 0 20M12 2c-3 3-3 17 0 20M4 7h16M4 17h16" fill="none" stroke="#fff" stroke-width="1.2"/></svg>
        www.brickafun.com
      </li>
    </ul>
  </section>
</body>
</html>
```